Kiss Wed or Run Show Flyer 2017

We are 3 female comedians who need to brand a new show that we want to take on the road. The show will be geared towards relationships. We will perform at clubs and theaters. We will also end up needing a logo etc for tee shirts and business cards and website. Etc. I am including some photos of the 3 of us from an old flyer from another show we did together ... it's not 'great' but it shows the 3 of us. ... perhaps there would be room for headshots also? or maybe we would add one shot of the 3 of us? There's also a chance we might want to include a 'guest' once in a while. The flyer should include space for the venue details and time date etc. and website. www.kisswedorrun-demo.net

Target Market(s)

Women. PG 13 and up. but not boxed in for just women. guys will have HUGE FUN TOO.

Logo Text

'Kiss Wed or Run'

Font styles to use
Sans Serif

Colors
e667a6
f04a50

Requirements
Must have
• Kiss Wed or Run
• possible tag lines- '3 comedians looking for love and finding the funny' or 'love means never having to say you're funny' or '3 funny women with choices'
• (we are still ironing out exactly the lines)
• names of 3 comedians: Nadia Pruitt, Odette Rue, Tessa Kolby
• space to easily edit venue name - date - time
Should not have
• no swirly bits. it should look strong and powerful but feminine.

```html
<!DOCTYPE html>
<html lang="en">
<head>
<meta charset="utf-8">
<title>Kiss Wed or Run – Show Flyer</title>
<link rel="stylesheet" href="https://fonts.googleapis.com/css2?family=Roboto+Slab:wght@700;800;900&display=swap">
<style>
  :root {
    --stage: #efbcb9;
    --paper: #ffffff;
    --rose: #f04a50;
    --orchid: #e667a6;
    --ink: #3a2f33;
    --slate: #8c8a90;
    --face-font: "Roboto Slab", "Arial Black", Arial, Helvetica, sans-serif;
  }
  * { margin: 0; padding: 0; box-sizing: border-box; }
  html, body { width: 800px; height: 1200px; overflow: hidden; }
  body {
    background: var(--stage);
    font-family: var(--face-font);
    position: relative;
  }
  .flyer {
    position: absolute;
    left: 60px; top: 220px;
    width: 680px; height: 760px;
    background: var(--paper);
    padding: 42px;
  }
  .flyer-face {
    position: relative;
    width: 596px; height: 676px;
    background: linear-gradient(135deg, var(--rose) 0%, var(--orchid) 100%);
    overflow: hidden;
  }
  .cast-photo {
    position: absolute;
    left: 20px; top: 0;
    width: 556px; height: 330px;
    background:
      radial-gradient(ellipse 22% 42% at 22% 42%, #f3d9c4 0%, rgba(243,217,196,0) 100%),
      radial-gradient(ellipse 22% 42% at 50% 42%, #e9b98f 0%, rgba(233,185,143,0) 100%),
      radial-gradient(ellipse 22% 42% at 78% 42%, #5a3444 0%, rgba(90,52,68,0) 100%);
  }
  .title-strip {
    position: absolute;
    left: 0; top: 332px;
    width: 596px; height: 40px;
    background: linear-gradient(90deg, var(--orchid) 0%, rgba(230,103,166,0.75) 60%, rgba(230,103,166,0.2) 100%);
  }
  .show-title {
    position: absolute;
    left: 0; top: 296px;
    width: 596px;
    text-align: center;
    font-family: var(--face-font);
    font-weight: 900;
    font-size: 58px;
    line-height: 74px;
    color: var(--paper);
    letter-spacing: -0.5px;
    white-space: nowrap;
  }
  .tagline-band {
    position: absolute;
    left: 0; top: 372px;
    width: 596px; height: 74px;
    background: linear-gradient(180deg, #ffffff 0%, #fbe3ec 55%, #efa7c4 100%);
    text-align: center;
    padding-top: 9px;
  }
  .tagline {
    font-weight: 800;
    font-size: 20px;
    line-height: 28px;
    color: var(--ink);
  }
  .cast-band {
    position: absolute;
    left: 0; top: 446px;
    width: 596px; height: 80px;
    background: linear-gradient(180deg, var(--slate) 0%, #b07a96 60%, var(--orchid) 100%);
    text-align: center;
    color: var(--paper);
    padding-top: 12px;
  }
  .cast-label { font-weight: 800; font-size: 16px; line-height: 24px; }
  .cast-names { font-weight: 800; font-size: 17px; line-height: 28px; white-space: nowrap; }
  .venue-box {
    position: absolute;
    left: 64px; top: 546px;
    width: 469px; height: 130px;
    background: var(--paper);
  }
  .venue-line {
    position: absolute;
    left: 38px; top: 104px;
    width: 382px; height: 1.5px;
    background: #555;
  }
</style>
</head>
<body>
  <div class="flyer">
    <div class="flyer-face">
      <div class="cast-photo" role="img" aria-label="Headshots of the three comedians side by side"></div>
      <div class="title-strip"></div>
      <h1 class="show-title">Kiss Wed or Run</h1>
      <div class="tagline-band">
        <p class="tagline">3 Comedians Looking For Love<br>And Finding The Funny</p>
      </div>
      <div class="cast-band">
        <p class="cast-label">Featuring:</p>
        <p class="cast-names">Nadia PRUITT , Tessa KOLBY &amp; Odette RUE</p>
      </div>
      <div class="venue-box" aria-label="Space for venue, date and time">
        <div class="venue-line"></div>
      </div>
    </div>
  </div>
</body>
</html>
```